VORLEN - Business Card Design Project

We need a business card design for a consultant company called VORLEN, LLC. (stands for Vendor Operations Resource Logic Engineering Network). The company provides Information Technology solutions, custom applications, services for financial and supply chain worldwide and focuses on business IT process improvements and all the steps leading to the procurement or integrating of any Enterprise related systems.

Industry/Entity Type

Financial

Requirements
Must have
• - In the submitted proposed version you should have one variant with black background and one with white.
The designer should show the shadow element of the company name in binary code (010101100100111101010010010011000100010101001110). It can be in one line or split in two

In your example please use the following info
Derek Holloway
Principal Consultant
dholloway@vorlenmail.net
+1 (000) 000 - 0000

Please keep in mind that the design should have some spaces to add the second phone and/or web site name
Nice to have
• Since this IT company and is working closely with Accounting and Logistics Application you can add some elements (contour only) of these types of the bussines as well (for example some $ or euro sign or truck or warehouse element)
Should not have
• Don’t use any extra color that is not in the company color logo pattern

```html
<!DOCTYPE html>
<html lang="en">
<head>
<meta charset="utf-8">
<title>VORLEN – Business Cards</title>
<link href="https://fonts.googleapis.com/css2?family=Arimo:wght@400;700&family=Open+Sans:wght@400;600&display=swap" rel="stylesheet">
<style>
  :root {
    --page: #ffffff;
    --ink: #111111;
    --card-dark: #050505;
    --binary: #1a1a1a;
    --white: #ffffff;
    --sky: #29a3de;
    --gold: #f3b31b;
    --green: #2e9a46;
    --grey: #333333;
  }
  * { margin: 0; padding: 0; box-sizing: border-box; }
  html, body { width: 1200px; height: 901px; overflow: hidden; background: var(--page); }
  .canvas { position: relative; width: 1200px; height: 901px; }

  .card {
    position: absolute;
    left: 263px;
    width: 653px;
    height: 375px;
    overflow: hidden;
    box-shadow: 3px 4px 8px rgba(0,0,0,0.35);
  }
  .card--front { top: 43px; background: var(--card-dark); }
  .card--back { top: 484px; background: var(--white); }

  .binary {
    position: absolute; inset: 0;
    font-family: "Arimo", Arial, sans-serif;
    font-size: 34px;
    line-height: 36px;
    letter-spacing: 1px;
    color: var(--binary);
    white-space: nowrap;
    padding-top: 2px;
  }
  .binary span { display: block; }

  .brand-name {
    font-family: "Arimo", Arial, sans-serif;
    font-weight: 400;
    line-height: 1;
    white-space: nowrap;
  }
  .brand-tagline {
    font-family: "Arimo", Arial, sans-serif;
    line-height: 1;
    white-space: nowrap;
  }
  .brand-dot { position: absolute; border-radius: 50%; background: var(--sky); }

  .card--front .brand-dot { left: 48px; top: 160px; width: 48px; height: 48px; }
  .card--front .brand-name { position: absolute; left: 146px; top: 156px; font-size: 46px; letter-spacing: 2px; color: var(--white); }
  .card--front .brand-tagline { position: absolute; left: 148px; top: 200px; font-size: 9px; color: var(--white); }
  .card--front .web { position: absolute; left: 108px; top: 228px; font-family: "Arimo", Arial, sans-serif; font-size: 19px; letter-spacing: 1.5px; color: var(--white); }
  .ribbons { position: absolute; left: 400px; top: 70px; width: 253px; height: 305px; }

  .card--back .brand-dot { left: 56px; top: 60px; width: 80px; height: 80px; }
  .card--back .brand-name { position: absolute; left: 195px; top: 72px; font-size: 62px; letter-spacing: 5px; color: var(--ink); }
  .card--back .brand-tagline { position: absolute; left: 199px; top: 132px; font-size: 13.5px; color: var(--ink); }

  .person {
    position: absolute; left: 48px; top: 252px; width: 307px;
    text-align: center; font-family: "Open Sans", Arial, sans-serif;
  }
  .person__name { font-size: 25px; font-weight: 600; color: var(--sky); line-height: 34px; }
  .person__rule { height: 2px; background: var(--gold); margin: 2px 0 6px; }
  .person__role { font-size: 16px; color: var(--grey); }

  .contacts {
    position: absolute; left: 420px; top: 250px; list-style: none;
    font-family: "Open Sans", Arial, sans-serif; font-size: 16px; color: var(--grey);
  }
  .contacts li { display: flex; align-items: center; height: 21.5px; }
  .contacts svg { width: 14px; height: 14px; margin-right: 8px; fill: var(--green); }

  .stripe { position: absolute; left: 0; bottom: 0; width: 653px; height: 14px; }
</style>
</head>
<body>
<div class="canvas">

  <section class="card card--front">
    <div class="binary" aria-hidden="true">
      <span>010101100100111101010010010011000100010101001110</span>
      <span>001001111010100100110001000101010011100101011001</span>
      <span>010101100100111101010010010011000100010101001110</span>
      <span>110010011110101001001100010001010100111001010110</span>
      <span>010101100100111101010010010011000100010101001110</span>
      <span>001001111010100100110001000101010011100101011001</span>
      <span>010101100100111101010010010011000100010101001110</span>
      <span>110010011110101001001100010001010100111001010110</span>
      <span>010101100100111101010010010011000100010101001110</span>
      <span>001001111010100100110001000101010011100101011001</span>
    </div>
    <span class="brand-dot"></span>
    <div class="brand-name">VORLEN</div>
    <div class="brand-tagline">Vendor Operations Resource Logic Engineering Network</div>
    <div class="web">www.vorlen.net</div>
    <svg class="ribbons" viewBox="0 0 253 305" role="img" aria-label="Flowing line-art ribbons in blue, orange and green">
      <defs>
        <linearGradient id="ribbonFill" x1="0" y1="0" x2="0.6" y2="1">
          <stop offset="0" stop-color="#1f5fb8"/>
          <stop offset="0.35" stop-color="#29a3de"/>
          <stop offset="0.55" stop-color="#f7941d"/>
          <stop offset="0.75" stop-color="#b5d334"/>
          <stop offset="1" stop-color="#6bbf3f"/>
        </linearGradient>
        <filter id="ribbonSoft" x="-20%" y="-20%" width="140%" height="140%">
          <feGaussianBlur stdDeviation="10"/>
        </filter>
      </defs>
      <path d="M40 130 C90 60 170 25 253 15 L253 305 L95 305 C60 270 40 220 45 180 C70 170 60 150 40 130 Z"
            fill="url(#ribbonFill)" opacity="0.75" filter="url(#ribbonSoft)"/>
    </svg>
  </section>

  <section class="card card--back">
    <span class="brand-dot"></span>
    <div class="brand-name">VORLEN</div>
    <div class="brand-tagline">Vendor Operations Resource Logic Engineering Network</div>

    <div class="person">
      <div class="person__name">Derek Holloway</div>
      <div class="person__rule"></div>
      <div class="person__role">Principal Consultant</div>
    </div>

    <ul class="contacts">
      <li><svg viewBox="0 0 24 24" aria-hidden="true"><path d="M6.6 10.8a15 15 0 0 0 6.6 6.6l2.2-2.2a1 1 0 0 1 1-.25 11.4 11.4 0 0 0 3.6.57 1 1 0 0 1 1 1V20a1 1 0 0 1-1 1A17 17 0 0 1 3 4a1 1 0 0 1 1-1h3.5a1 1 0 0 1 1 1c0 1.25.2 2.45.57 3.57a1 1 0 0 1-.25 1z"/></svg>+1 (000) 000 - 0000</li>
      <li><svg viewBox="0 0 24 24" aria-hidden="true"><path d="M7 1h10a2 2 0 0 1 2 2v18a2 2 0 0 1-2 2H7a2 2 0 0 1-2-2V3a2 2 0 0 1 2-2zm0 3v14h10V4zm5 15.5a1.2 1.2 0 1 0 0 2.4 1.2 1.2 0 0 0 0-2.4z"/></svg>+1 (000) 000 - 0000</li>
      <li><svg viewBox="0 0 24 24" aria-hidden="true"><path d="M2 5h20v14H2zm2 2v.5l8 5 8-5V7zm0 2.8V17h16V9.8l-8 5z"/></svg>dholloway@vorlenmail.net</li>
      <li><svg viewBox="0 0 24 24" aria-hidden="true"><path d="M12 2a10 10 0 1 0 0 20 10 10 0 0 0 0-20zm6.9 6h-3a15.6 15.6 0 0 0-1.4-3.6A8 8 0 0 1 18.9 8zM12 4c.8 1.2 1.5 2.5 1.9 4h-3.8c.4-1.5 1.1-2.8 1.9-4zM4.3 14a8 8 0 0 1 0-4h3.4a16 16 0 0 0 0 4zm.8 2h3a15.6 15.6 0 0 0 1.4 3.6A8 8 0 0 1 5.1 16zm3-8h-3a8 8 0 0 1 4.4-3.6A15.6 15.6 0 0 0 8.1 8zM12 20c-.8-1.2-1.5-2.5-1.9-4h3.8c-.4 1.5-1.1 2.8-1.9 4zm2.3-6H9.7a14 14 0 0 1 0-4h4.6a14 14 0 0 1 0 4zm.2 5.6a15.6 15.6 0 0 0 1.4-3.6h3a8 8 0 0 1-4.4 3.6zm1.8-5.6a16 16 0 0 0 0-4h3.4a8 8 0 0 1 0 4z"/></svg>www.vorlen.net</li>
    </ul>

    <svg class="stripe" viewBox="0 0 653 14" preserveAspectRatio="none" aria-hidden="true">
      <defs>
        <linearGradient id="bandBlue" x1="0" x2="1"><stop offset="0" stop-color="#29a3de"/><stop offset="1" stop-color="#1f3f95"/></linearGradient>
        <linearGradient id="bandOrange" x1="0" x2="1"><stop offset="0" stop-color="#f7941d"/><stop offset="1" stop-color="#e5322d"/></linearGradient>
        <linearGradient id="bandGreen" x1="0" x2="1"><stop offset="0" stop-color="#d7e23a"/><stop offset="1" stop-color="#2e9a46"/></linearGradient>
      </defs>
      <rect width="653" height="14" fill="#111111"/>
      <polygon points="48,0 237,0 231,14 42,14" fill="url(#bandBlue)"/>
      <polygon points="244,0 421,0 415,14 238,14" fill="url(#bandOrange)"/>
      <polygon points="428,0 606,0 600,14 422,14" fill="url(#bandGreen)"/>
    </svg>
  </section>

</div>
</body>
</html>
```